Funky physio needs a business card to match!

We are a physiotherapy clinic and pilates studio who specialise in sports and spinal injuries, as well as persistent or chronic pain.

We would like a vibrant and fun business card which is not over medicalised.
Updates

PO Box number is 418

Industry/Entity Type

Clinic

Contact Information for Business Card

Tidewell Sports Medicine
Suite 1 & 2 Marlowe St, BRAMLEIGH VIC 3190
p 86203917
f 9481 3057
e admin@tidewellsportsmedicine.com.au
w tidewellsportsmedicine.com.au

All correspondence via email or mailed to:
PO Box
BRAMLEIGH VIC 3190

Requirements
Must have
• Must have a green element - see logo. I don't mind if the business card is green, or if it's black, grey, white etc with green highlights. I'm the physio ... you're the designer!!!! It just needs to "look" green!
Our font is Harabara and can be downloaded from glyphbarn.com
Nice to have
• Please check our website to get a feel of our company. We don't take ourselves to seriously, however want to be taken seriously!
Should not have
• not over medicalised or corporate

```html
<!DOCTYPE html>
<html lang="en">
<head>
<meta charset="utf-8">
<title>Tidewell Sports Medicine – Business Card</title>
<link rel="stylesheet" href="https://fonts.googleapis.com/css2?family=Nunito:wght@800&family=Source+Sans+3:wght@400&display=swap">
<style>
  :root {
    --page-bg: #ffffff;
    --card-deep: #3b5612;
    --card-mid: #4e6b1f;
    --card-glow: #8f9d72;
    --lime: #9acb3c;
    --text-light: #ffffff;
  }
  html, body {
    margin: 0;
    width: 1200px;
    height: 1000px;
    overflow: hidden;
    background: var(--page-bg);
  }
  .business-card {
    position: absolute;
    left: 80px;
    top: 202px;
    width: 1040px;
    height: 590px;
    overflow: hidden;
    background:
      radial-gradient(circle at 790px 230px, var(--card-glow) 0, var(--card-mid) 260px, var(--card-deep) 560px),
      var(--card-deep);
  }
  .brand-name {
    position: absolute;
    left: 64px;
    top: 40px;
    margin: 0;
    font-family: "Nunito", sans-serif;
    font-weight: 800;
    font-size: 68px;
    line-height: 80px;
    letter-spacing: -0.5px;
    color: var(--lime);
  }
  .brand-name .line-two { color: var(--text-light); }
  .divider {
    position: absolute;
    left: 65px;
    top: 208px;
    width: 975px;
    height: 3px;
    background: var(--lime);
  }
  .brand-mark {
    position: absolute;
    left: 700px;
    top: 120px;
    width: 280px;
    margin: 0;
    text-align: center;
    font-family: "Source Sans 3", sans-serif;
    font-weight: 400;
    font-size: 44px;
    line-height: 50px;
    color: var(--lime);
  }
  .contact-details {
    position: absolute;
    left: 67px;
    top: 222px;
    margin: 0;
    font-family: "Source Sans 3", sans-serif;
    font-style: normal;
    font-weight: 400;
    font-size: 29px;
    line-height: 40px;
    color: var(--text-light);
    letter-spacing: -0.4px;
  }
  .contact-details p { margin: 0; }
  .contact-details .indent { padding-left: 34px; }
  .contact-details .gap { margin-top: 5px; }
  .contact-details .label { margin-right: 10px; }
</style>
</head>
<body>
  <section class="business-card">
    <h1 class="brand-name">Tidewell Sports<br><span class="line-two">Medicine</span></h1>

    <p class="brand-mark">Tidewell</p>

    <div class="divider"></div>

    <address class="contact-details">
      <p>Suite 1 &amp; 2 Marlowe St,</p>
      <p class="indent">BRAMLEIGH VIC 3190</p>
      <p class="gap"><span class="label">Phone:</span>86203917</p>
      <p><span class="label">Fax No.</span>9481 3057</p>
      <p class="gap"><span class="label">Email:</span>admin@tidewellsportsmedicine.com.au</p>
      <p class="gap"><span class="label">Website:</span>tidewellsportsmedicine.com.au</p>
      <p class="gap">All correspondence via email or mailed to:</p>
      <p class="indent">PO Box BRAMLEIGH VIC 3190</p>
    </address>
  </section>
</body>
</html>
```